BLUE DUSK MOVIE POSTER a dramatic film

We need a movie poster design for a dramatic film about immigration and DRA police. The film is about Mateo Villalba a father and husband, who’s an illegal immigrant. He avoids deportation by going on the run with his American wife. Things get complicated when the DRA officer Briggs kills his partner and frames Mateo for the murder.

Target Market(s)

US, Latin America

Industry/Entity Type

Film Production

Requirements
Must have
• The project must the title BLUE DUSK on the poster in all caps. The project should be in a standard movie poster size of 27x40” in portrait format.

```html
<!DOCTYPE html>
<html lang="en">
<head>
<meta charset="utf-8">
<title>BLUE DUSK — Movie Poster</title>
<link href="https://fonts.googleapis.com/css2?family=Alfa+Slab+One&family=Bebas+Neue&family=Libre+Baskerville&family=Permanent+Marker&display=swap" rel="stylesheet">
<style>
  :root {
    --backdrop: #8e9aaa;
    --poster: #1f3441;
    --ink-light: #f4f1ec;
    --portrait-warm: #8a5a44;
    --portrait-deep: #3a2622;
    --portrait-skin: #c89a80;
    --street-night: #3b3530;
    --street-glow: #9a6a48;
  }
  * { margin: 0; padding: 0; box-sizing: border-box; }
  html, body {
    width: 1200px;
    height: 1200px;
    overflow: hidden;
    background: var(--backdrop);
  }
  .poster {
    position: absolute;
    left: 276px;
    top: 120px;
    width: 648px;
    height: 955px;
    background: var(--poster);
    overflow: hidden;
  }
  .tagline {
    position: absolute;
    left: 0;
    width: 100%;
    top: 270px;
    text-align: center;
    font-family: "Bebas Neue", sans-serif;
    font-size: 21px;
    letter-spacing: 3.4px;
    color: var(--ink-light);
  }
  .title-art {
    position: absolute;
    left: 0;
    top: 0;
    width: 648px;
    height: 955px;
  }
  .title-main {
    font-family: "Alfa Slab One", serif;
    font-size: 180px;
  }
  .title-brush {
    font-family: "Permanent Marker", cursive;
    font-size: 128px;
  }
  .release {
    position: absolute;
    left: 0;
    width: 100%;
    top: 852px;
    text-align: center;
    font-family: "Libre Baskerville", serif;
    font-size: 27px;
    letter-spacing: 2.5px;
    color: var(--ink-light);
  }
</style>
</head>
<body>
  <main class="poster">
    <p class="tagline">A dramatic film about immigration and DRA police</p>

    <svg class="title-art" viewBox="0 0 648 955" role="img" aria-label="Film title BLUE DUSK, letters filled with portraits of the cast and a night street scene">
      <defs>
        <linearGradient id="portrait-fill" x1="0" y1="0" x2="1" y2="0.3">
          <stop offset="0" stop-color="var(--portrait-deep)"/>
          <stop offset="0.3" stop-color="var(--portrait-skin)"/>
          <stop offset="0.55" stop-color="var(--portrait-warm)"/>
          <stop offset="0.8" stop-color="var(--portrait-skin)"/>
          <stop offset="1" stop-color="var(--portrait-deep)"/>
        </linearGradient>
        <linearGradient id="street-fill" x1="0" y1="0" x2="1" y2="1">
          <stop offset="0" stop-color="var(--street-glow)"/>
          <stop offset="0.5" stop-color="var(--street-night)"/>
          <stop offset="1" stop-color="var(--portrait-warm)"/>
        </linearGradient>
      </defs>
      <text class="title-main" x="75" y="443" textLength="502" lengthAdjust="spacingAndGlyphs" fill="url(#portrait-fill)">BLUE</text>
      <polygon class="title-brush-bar" points="418,484 648,478 648,498 420,502" fill="url(#street-fill)"/>
      <text class="title-brush" x="300" y="632" textLength="236" lengthAdjust="spacingAndGlyphs" fill="url(#street-fill)">DUSK</text>
    </svg>

    <p class="release">COMING SOON</p>
  </main>
</body>
</html>
```